Transform Your Giving

I need a tri-fold brochure that will fit in a standard number 10 business envelope. Harborline and Caring Works is a charitable nonprofit. The goal of this brochure is to stimulate people into thinking about other ways to make a donation. The design should communicate the essential information on donation options, create a sense of professional integrity, be graphically sharp, easy to read and laid out in a way that doesn't make the material appear crowded.

```html
<!DOCTYPE html>
<html lang="en">
<head>
<meta charset="utf-8">
<title>Transform Your Giving – Tri-fold Brochure</title>
<link href="https://fonts.googleapis.com/css2?family=Montserrat:wght@500;600;700;800;900&family=Open+Sans:ital,wght@0,400;0,600;0,700;1,400;1,600&display=swap" rel="stylesheet">
<style>
:root{
  --navy:#1f2a5c;
  --green:#5fa83a;
  --green-light:#8cc63f;
  --ink:#333842;
  --paper:#ffffff;
  --stage:#e9ebef;
  --photo-warm:#c9b49a;
  --photo-cool:#aebac4;
}
*{box-sizing:border-box;margin:0;padding:0}
html,body{width:1200px;height:3572px;overflow:hidden;background:var(--stage)}
body{font-family:"Open Sans",Arial,sans-serif;color:var(--ink);position:relative}
.spread{position:absolute;left:0;width:1200px;height:927px;display:grid;grid-template-columns:repeat(3,400px);background:var(--paper);box-shadow:0 6px 24px rgba(20,30,60,.18);overflow:hidden}
.spread--outside{top:1700px}
.spread--inside{top:2640px}
.panel{position:relative;height:927px;overflow:hidden}
.panel + .panel{border-left:1px solid #e3e5ea}
h2,h3,h4{font-family:"Montserrat",Arial,sans-serif}
.body-text{font-size:11.5px;line-height:1.6;color:var(--ink)}
.body-text + .body-text{margin-top:9px}
.photo{position:absolute;left:0;width:400px}
.curve{position:absolute;left:0;width:400px;display:block}

/* outside – impact panel */
.impact .topbar{height:16px;background:var(--navy)}
.impact .content{padding:30px 34px 0}
.impact h2{color:var(--navy);font-size:21px;font-weight:800;letter-spacing:.3px;margin-bottom:16px}
.gift-list{list-style:none;margin-top:18px}
.gift-list li{font-family:"Montserrat",Arial,sans-serif;font-weight:700;color:var(--navy);font-size:16px;display:flex;align-items:center;gap:12px;margin-bottom:9px}
.gift-list li::before{content:"";width:11px;height:11px;border-radius:50%;background:var(--green);flex:none}
.impact .photo{top:520px;height:407px;background:linear-gradient(160deg,var(--photo-cool),var(--photo-warm) 70%,#9a7d64)}

/* outside – contact panel */
.contact{background:var(--navy);color:#fff;padding:26px 34px}
.contact .follow{font-family:"Montserrat",Arial,sans-serif;font-weight:700;font-size:14px;margin-bottom:30px}
.contact .fine{font-size:10px;line-height:1.55;color:#d3d8ea;margin-bottom:12px}
.contact .lead{font-size:11px;line-height:1.6;margin:18px 0 16px;font-weight:600}
.contact .quote{font-style:italic;font-size:13px;line-height:1.5;color:var(--green-light);font-weight:600}
.contact .quote-by{font-family:"Montserrat",Arial,sans-serif;font-style:italic;font-weight:800;font-size:16px;margin:4px 0 18px}
.contact .will{font-size:11px;line-height:1.55;text-align:center}
.contact .will strong{display:block;font-size:15px;margin:3px 0}
.contact h3{font-size:17px;font-weight:800;text-align:center;margin:20px 0 8px;letter-spacing:.5px}
.contact .address{font-size:11px;line-height:1.6;text-align:center}
.contact .phone{font-family:"Montserrat",Arial,sans-serif;font-size:24px;font-weight:800;text-align:center;margin:16px 0 6px}
.contact .web{font-size:11px;text-align:center;color:#d3d8ea}

/* outside – cover */
.cover{text-align:center}
.brand{display:flex;align-items:center;justify-content:center;gap:10px;margin-top:44px}
.brand-dot{width:22px;height:22px;border-radius:50%;background:var(--green)}
.brand-name{font-family:"Montserrat",Arial,sans-serif;font-weight:900;font-size:38px;color:var(--navy);letter-spacing:2px}
.brand-sub{font-size:8.5px;letter-spacing:1.2px;color:var(--navy);text-transform:uppercase;margin-top:4px}
.cover .kicker{font-family:"Montserrat",Arial,sans-serif;font-weight:600;font-size:20px;color:var(--navy);margin-top:32px}
.cover h1{font-family:"Montserrat",Arial,sans-serif;font-weight:900;color:var(--green);font-size:40px;line-height:1.02;margin-top:8px}
.cover .tagline{font-size:13px;line-height:1.45;color:var(--navy);font-weight:600;margin:12px 38px 0}
.cover .photo{top:430px;height:497px;background:linear-gradient(170deg,#dfe3e8,var(--photo-warm) 80%)}

/* inside */
.intro .photo{top:0;height:300px;background:linear-gradient(150deg,var(--photo-cool),var(--photo-warm))}
.intro .content{position:absolute;top:318px;left:0;right:0;padding:0 32px}
.section-title{font-size:17px;font-weight:800;line-height:1.2;margin:16px 0 6px}
.section-title.green{color:var(--green)}
.lead-italic{font-style:italic;font-weight:600;font-size:11.5px;line-height:1.5;color:var(--green);margin-bottom:8px}
.how{font-size:18px;font-weight:800;color:var(--navy);margin:14px 0 6px}

.daf .topbar{height:16px;background:var(--navy)}
.daf .content{padding:26px 32px 0}
.daf h2{font-size:20px;font-weight:800;color:var(--navy);line-height:1.2;margin-bottom:10px}
.qcd{position:absolute;left:0;right:0;top:610px;bottom:0;background:var(--green);color:#fff;padding:22px 32px}
.qcd h3{font-size:16px;font-weight:800;line-height:1.2;margin-bottom:8px}
.qcd .body-text{color:#fff;font-size:10.5px;line-height:1.5}
.qcd .lead-italic{color:#f2fbe8}

.crypto .photo{top:0;height:250px;background:linear-gradient(160deg,#d6dbe2,var(--photo-warm))}
.crypto .content{position:absolute;top:262px;left:0;right:0;padding:0 30px}
.crypto .body-text{font-size:10.5px;line-height:1.5}
.crypto .how{font-size:14px;margin:8px 0 4px}
.crypto .section-title{font-size:15px;margin:10px 0 4px}
.ticks{list-style:none;margin:6px 0}
.ticks li{font-size:10.5px;line-height:1.45;padding-left:16px;position:relative;margin-bottom:4px}
.ticks li::before{content:"";position:absolute;left:2px;top:5px;width:7px;height:7px;border-radius:50%;background:var(--green)}
</style>
</head>
<body>

<section class="spread spread--outside" aria-label="Brochure outside">
  <article class="panel impact">
    <div class="topbar"></div>
    <div class="content">
      <h2>THE IMPACT OF YOUR GIFT</h2>
      <p class="body-text">Your generosity drives our mission. With every gift, you help Harborline and Caring Works protect and support vulnerable adults across our state. Smart giving lets your dollars stretch further, often with tax benefits for you and lasting impact for those we serve. Explore the options below and find the fit for your plans.</p>
      <ul class="gift-list">
        <li>Stocks and Securities</li>
        <li>DAFs</li>
        <li>QCDs</li>
        <li>Crypto</li>
        <li>Charitable Annuity</li>
      </ul>
    </div>
    <div class="photo" role="img" aria-label="Photo of a smiling grandfather and grandmother hugging their granddaughter"></div>
    <svg class="curve" style="top:827px" width="400" height="100" viewBox="0 0 400 100" aria-hidden="true">
      <path d="M0 50 C120 10 260 90 400 30 L400 100 L0 100Z" fill="#5fa83a"/>
      <path d="M0 72 C140 40 260 100 400 62 L400 100 L0 100Z" fill="#1f2a5c"/>
    </svg>
  </article>

  <article class="panel contact">
    <p class="follow">Follow us</p>
    <p class="fine">This material is provided for informational purposes only and is not intended as legal, tax or financial advice. Please consult with your own advisor before making any charitable gift.</p>
    <p class="lead">To learn more about Smart Giving options and how they can benefit you and Harborline and Caring Works, please reach out to us. We'd love to help you navigate these giving methods and answer any questions you may have.</p>
    <p class="quote">Being kind to others is a way of being good to yourself.</p>
    <p class="quote-by">Nora Whitfield</p>
    <p class="will">If you do not have a will, go to <strong>www.givingplan.example</strong> to get started on your free legal will – for free.</p>
    <h3>CONTACT US</h3>
    <p class="address">Have more questions? Please contact us at<br>Harborline and Caring Works.<br><br>412 Alder Row, Suite 6 • Fairhaven, ND 58000</p>
    <p class="phone">555-014-2200 (ext. 100)</p>
    <p class="web">giving@harborlinecw.org &nbsp;|&nbsp; www.harborlinecw.org</p>
  </article>

  <article class="panel cover">
    <div class="brand"><span class="brand-dot"></span><span class="brand-name">HCW</span></div>
    <p class="brand-sub">Harborline and Caring Works</p>
    <p class="kicker">Transform Your Giving</p>
    <h1>BE STRATEGIC,<br>BE SMART</h1>
    <p class="tagline">Discover the Impact of Smart Giving with Harborline and Caring Works</p>
    <div class="photo" role="img" aria-label="Photo of a smiling man holding a glass jar of coins"></div>
    <svg class="curve" style="top:800px" width="400" height="127" viewBox="0 0 400 127" aria-hidden="true">
      <path d="M0 40 C130 110 270 0 400 50 L400 127 L0 127Z" fill="#8cc63f"/>
      <path d="M0 70 C140 120 280 30 400 80 L400 127 L0 127Z" fill="#5fa83a"/>
      <path d="M0 100 C150 130 280 80 400 105 L400 127 L0 127Z" fill="#1f2a5c"/>
    </svg>
  </article>
</section>

<section class="spread spread--inside" aria-label="Brochure inside">
  <article class="panel intro">
    <div class="photo" role="img" aria-label="Photo of an older man and woman holding a donation box"></div>
    <svg class="curve" style="top:250px" width="400" height="60" viewBox="0 0 400 60" aria-hidden="true">
      <path d="M0 20 C130 60 260 0 400 30 L400 60 L0 60Z" fill="#5fa83a"/>
      <path d="M0 40 C140 64 270 20 400 46 L400 60 L0 60Z" fill="#ffffff"/>
    </svg>
    <div class="content">
      <p class="body-text">We would like to introduce you to five Strategic and Smart ways to give that can be more rewarding for you and more beneficial to the clients we serve. Each option offers unique advantages. We encourage you to keep this brochure as a guide for your future contributions.</p>
      <h3 class="section-title green">Gifts of Stocks or Appreciated Assets Strategic &amp; Smart</h3>
      <p class="lead-italic">Consider your long-term publicly traded stock as a way to give to your favorite charity.</p>
      <p class="body-text">You can make a significantly bigger impact when you donate long-term appreciated securities, including stock, mutual funds and bonds, directly to your favorite charity.</p>
      <h4 class="how">How Does It Work?</h4>
      <p class="body-text">When you donate stock to a charity, you will generally take a tax deduction for its full market value. Because you are donating stock, your contribution and tax deduction may be larger than if you sold the stock and donated after-tax proceeds.</p>
    </div>
  </article>

  <article class="panel daf">
    <div class="topbar"></div>
    <div class="content">
      <h2>Donor-Advised Fund (DAF)<br>Strategic &amp; Smart</h2>
      <p class="lead-italic">Consider a DAF – a simple, flexible, and tax-advantaged way to give to your favorite charities.</p>
      <p class="body-text">A Donor-Advised Fund (DAF) is a charitable investment account for the sole purpose of supporting your favorite charities.</p>
      <h4 class="how">How Does It Work?</h4>
      <p class="body-text">You establish a DAF and contribute cash, stocks or non-publicly traded assets such as cryptocurrency, and private company stock to be eligible for an immediate tax deduction. Then you can recommend grants from the fund to the charities you love over time.</p>
    </div>
    <svg class="curve" style="top:560px" width="400" height="52" viewBox="0 0 400 52" aria-hidden="true">
      <path d="M0 52 C120 0 280 10 400 40 L400 52Z" fill="#5fa83a"/>
    </svg>
    <div class="qcd">
      <h3>Qualified Charitable Distributions (QCDs) Strategic &amp; Smart</h3>
      <p class="lead-italic">Consider a QCD – your opportunity to give tax-free from your IRA to the charities you care about.</p>
      <p class="body-text">A Qualified Charitable Distribution lets you transfer funds directly from your IRA to a qualified charity, satisfying some or all of your required minimum distribution.</p>
      <p class="body-text">How it works: If you are 70½ or older, you can give up to the annual limit directly from your IRA. The amount is excluded from your taxable income, which may lower your overall tax bill.</p>
    </div>
  </article>

  <article class="panel crypto">
    <div class="photo" role="img" aria-label="Photo of a smiling woman holding a donation box"></div>
    <svg class="curve" style="top:215px" width="400" height="50" viewBox="0 0 400 50" aria-hidden="true">
      <path d="M0 30 C130 0 270 50 400 14 L400 50 L0 50Z" fill="#5fa83a"/>
      <path d="M0 42 C140 18 270 56 400 30 L400 50 L0 50Z" fill="#ffffff"/>
    </svg>
    <div class="content">
      <h3 class="section-title green">Cryptocurrency Strategic &amp; Smart</h3>
      <p class="lead-italic">Consider donating digital currency and other cryptocurrencies to your favorite charity.</p>
      <p class="body-text">Digital currency and other cryptocurrencies can be donated just like stock. When held more than a year, you may deduct the full fair market value and avoid capital gains.</p>
      <h4 class="how">How Does It Work?</h4>
      <p class="body-text">Many donors find it useful to give cryptocurrency directly rather than selling it first. This strategy includes two significant benefits:</p>
      <ul class="ticks">
        <li>Your donation may be deductible at full fair market value.</li>
        <li>You can eliminate capital gains taxes on the amount donated, leaving more for the charity.</li>
      </ul>
      <p class="body-text">Other charities may not accept crypto, so asking us first is a good way to donate.</p>
      <h3 class="section-title green">Charitable Gift Annuity Strategic &amp; Smart</h3>
      <p class="lead-italic">Consider establishing a Charitable Gift Annuity</p>
      <p class="body-text">You make a donation to a single charity. The gift is set aside in a reserve account and invested.</p>
      <h4 class="how">How Does It Work?</h4>
      <p class="body-text">A charitable gift annuity is a contract between a donor and a charity. As a donor, you make a gift to charity using cash, securities or property, and in return receive fixed payments for life.</p>
      <p class="body-text">In return, you become eligible for a partial tax deduction, and the remaining gift passes to the charity upon your passing.</p>
    </div>
  </article>
</section>

</body>
</html>
```